Invitation - Melbourne Show Invitation

We need an e-Invitation for our Trade Show in Melbourne. We are holding a furniture show at our Melbourne Showroom:

The Brindlewood Private Show

Dates: Wednesday 19th to Friday 21st July

Hours: 9am to 6pm

Join us for Drinks on Thursday 20th from 5pm

Address:
The Lantern Room
47 Dunmore Street
Melbourne

RSVP: rosalind@brindlewood-au.com

Tel. 03 9555 0182

The style of the building and the furniture is mid-century design, so I would like the invitation to reflect this (think "Tin Harbor").

Target Market(s)

Professional Retailers

Industry/Entity Type

Trade

Font styles to use
Sans Serif

Colors

Designer to choose colors to be used in the design.

Requirements
Must have
• Dates and Times

```html
<!DOCTYPE html>
<html lang="en">
<head>
<meta charset="utf-8">
<title>The Brindlewood Private Show – Melbourne Invitation</title>
<link rel="stylesheet" href="https://fonts.googleapis.com/css2?family=Lato:wght@300;400;700;900&display=swap">
<style>
  :root {
    --orange: #ef7a22;
    --ink: #2b2424;
    --olive: #3e3f2c;
    --paper: #f6f4ef;
    --backdrop: #dcdce0;
  }
  * { margin: 0; padding: 0; box-sizing: border-box; }
  html, body {
    width: 1200px; height: 1200px; overflow: hidden;
    background: var(--backdrop);
    font-family: "Lato", sans-serif;
  }
  .invitation {
    position: absolute; left: 0; top: 146px;
    width: 1200px; height: 908px;
    background: var(--paper);
    color: var(--ink);
  }
  .edge-band {
    position: absolute; right: 0; top: 0;
    width: 84px; height: 100%;
    background: var(--orange);
  }
  .brand-name {
    position: absolute; left: 112px; top: 205px; width: 420px;
    font-weight: 900; font-size: 52px; line-height: 62px;
    color: var(--ink);
  }
  .furniture-art {
    position: absolute; left: 76px; top: 428px;
    width: 480px; height: 180px;
    background: linear-gradient(90deg, #e9e6df 0%, #d9d5cb 40%, #e7d3c1 70%, #dcd8ce 100%);
    border-radius: 6px;
  }
  .city-tag {
    position: absolute; left: 94px; top: 627px;
    width: 442px; height: 60px;
    background: var(--orange);
    color: #fff; font-weight: 300; font-size: 34px;
    line-height: 60px; text-align: center;
  }
  .city-rule {
    position: absolute; left: 94px; top: 691px;
    width: 442px; height: 3px; background: var(--olive);
  }
  .divider {
    position: absolute; left: 599px; top: 202px;
    width: 2px; height: 504px; background: var(--orange);
  }
  .details {
    position: absolute; right: 123px; top: 148px; width: 460px;
    text-align: right; font-weight: 300;
  }
  .details p { white-space: nowrap; }
  .intro { font-size: 22px; line-height: 26px; }
  .event-title { font-size: 36px; line-height: 46px; }
  .rule { height: 2px; background: var(--orange); margin-left: 40px; }
  .rule.first { margin-top: 12px; }
  .day { color: var(--orange); font-weight: 400; font-size: 34px; line-height: 44px; margin-top: 6px; }
  .dates { color: var(--orange); font-weight: 400; font-size: 70px; line-height: 70px; letter-spacing: -1px; }
  .dates sup { font-size: 38px; vertical-align: 26px; }
  .dates .joiner { font-size: 30px; margin: 0 8px; }
  .hours { color: var(--orange); font-weight: 400; font-size: 34px; line-height: 44px; padding-right: 15px; margin-bottom: 12px; }
  .drinks { font-size: 36px; line-height: 43px; margin-top: 12px; }
  .drinks sup { font-size: 20px; vertical-align: 14px; }
  .address-label { color: var(--orange); font-weight: 400; font-size: 28px; line-height: 34px; text-decoration: underline; margin-top: 12px; }
  .address { font-size: 26px; line-height: 34px; }
  .contact { font-size: 26px; line-height: 33px; margin-top: 12px; }
</style>
</head>
<body>
  <main class="invitation">
    <div class="brand-name">The Brindlewood<br>Private Show</div>
    <div class="furniture-art" role="img" aria-label="Illustration of a mid-century armchair and two-seat sofa with orange cushions"></div>
    <div class="city-tag">Melbourne</div>
    <div class="city-rule"></div>

    <div class="divider"></div>

    <section class="details">
      <p class="intro">You are cordially invited to</p>
      <p class="event-title">The Brindlewood Private Show</p>
      <div class="rule first"></div>
      <p class="day">Wednesday</p>
      <p class="dates">19<sup>th</sup><span class="joiner">to</span>21<sup>st</sup> July</p>
      <p class="hours">9am to 6pm</p>
      <div class="rule"></div>
      <p class="drinks">Join us for Drinks on<br>Thursday 20<sup>th</sup> from 5pm</p>
      <p class="address-label">Address</p>
      <p class="address">The Lantern Room<br>47 Dunmore Street<br>Melbourne</p>
      <p class="contact">RSVP: rosalind@brindlewood-au.com<br>Tel. 03 9555 0182</p>
    </section>

    <div class="edge-band"></div>
  </main>
</body>
</html>
```